Brevin Law Client Handbook

We are a small, rapidly growing, criminal defense law firm located in a suburb of Seattle, WA. The cover should be professional and be consistent with our image a sleek, modern, and efficient. The included files show our designs used in other projects for reference.

```html
<!DOCTYPE html>
<html lang="en">
<head>
<meta charset="utf-8">
<title>Brevin Law Firm — Client Handbook</title>
<link href="https://fonts.googleapis.com/css2?family=Marcellus&family=Arimo:wght@400&display=swap" rel="stylesheet">
<style>
  :root {
    --backdrop: #1e1e1e;
    --navy: #0e3a58;
    --navy-deep: #0a3049;
    --navy-stripe: #164665;
    --paper: #ffffff;
    --mist: #dbe2e6;
    --ink: #123c5b;
    --statue-light: #c9d6e0;
  }
  html, body {
    margin: 0;
    width: 1200px;
    height: 995px;
    overflow: hidden;
    background: var(--backdrop);
  }
  .handbook-cover {
    position: absolute;
    left: 262px;
    top: 20px;
    width: 675px;
    height: 955px;
    display: block;
  }
  .wordmark-name {
    font-family: "Marcellus", "Times New Roman", serif;
    fill: var(--paper);
  }
  .cover-title {
    font-family: "Arimo", Arial, sans-serif;
    fill: var(--ink);
  }
</style>
</head>
<body>
<svg class="handbook-cover" viewBox="0 0 876 1240" xmlns="http://www.w3.org/2000/svg">
  <defs>
    <clipPath id="blue-field"><rect x="0" y="0" width="876" height="988"/></clipPath>
    <clipPath id="white-field"><rect x="0" y="988" width="876" height="252"/></clipPath>
    <linearGradient id="statue-tone" x1="0" y1="0" x2="1" y2="0">
      <stop offset="0" stop-color="var(--navy)" stop-opacity="0"/>
      <stop offset="0.55" stop-color="var(--statue-light)" stop-opacity="0.35"/>
      <stop offset="1" stop-color="var(--statue-light)" stop-opacity="0.55"/>
    </linearGradient>
  </defs>

  <!-- cover panels -->
  <rect class="cover-field" x="0" y="0" width="876" height="988" fill="var(--navy)"/>
  <rect class="cover-footer" x="0" y="988" width="876" height="252" fill="var(--paper)"/>

  <!-- chevron bands on navy -->
  <g class="chevron-bands" clip-path="url(#blue-field)">
    <polygon fill="var(--navy-deep)" points="532,0 702,0 172,625 702,1250 532,1250 2,625"/>
    <polygon fill="var(--navy-stripe)" points="702,0 722,0 192,625 722,1250 702,1250 172,625"/>
    <polygon fill="var(--navy-deep)" opacity="0.6" points="722,0 848,0 318,625 848,1250 722,1250 192,625"/>
  </g>

  <!-- chevron bands on footer -->
  <g class="footer-bands" clip-path="url(#white-field)">
    <polygon fill="var(--mist)" points="172,625 702,1250 532,1250 2,625"/>
    <polygon fill="var(--mist)" points="192,625 722,1250 848,1250 318,625"/>
  </g>

  <!-- statue of justice illustration area -->
  <rect class="statue-illustration" role="img" aria-label="Illustration of Lady Justice statue holding raised scales"
        x="560" y="30" width="316" height="958" fill="url(#statue-tone)"/>

  <!-- firm name -->
  <rect class="brand-square" x="142" y="565" width="86" height="112" fill="var(--paper)"/>
  <text class="wordmark-name" x="272" y="624" font-size="62" letter-spacing="15">BREVIN</text>
  <text class="wordmark-name" x="468" y="666" font-size="27" letter-spacing="4" text-anchor="middle">LAW FIRM</text>

  <!-- title -->
  <text class="cover-title" x="461" y="1128" font-size="34" letter-spacing="5.5" text-anchor="middle">CLIENT HANDBOOK</text>
</svg>
</body>
</html>
```